Ridge 4 Ridge Turbine Rentals Pty Ltd

We are a hire company based on the Gold Coast in Australia, we Hire out Generators to construction sites, music festivals, parties, fetes etc. Anywhere where power is required we can provide it.

Ridge 4 Ridge Turbine Rentals pty Ltd also provides all leads, distribution boards, Qualified Electricians to perform all connections. we offer refuelling services and mechanical services. 24Hr on call service - to an actual english speaking operator.

Slogan ''Current Wherever Needed"

Industry/Entity Type

Construction

Contact Information for Business Card

M: 0481265390
E: bookings@ridge4ridgeturbinerentals-example.com.au

```html
<!DOCTYPE html>
<html lang="en">
<head>
<meta charset="utf-8">
<title>Ridge 4 Ridge Turbine Rentals — Business Card</title>
<link rel="stylesheet" href="https://fonts.googleapis.com/css2?family=Open+Sans:wght@400;600;700&display=swap">
<style>
  :root {
    --page-bg: #e4e6e9;
    --card-bg: #ffffff;
    --ink: #1a1a1a;
    --ink-soft: #333333;
    --brand-deep: #1f6a96;
    --brand-light: #a5dcec;
    --brand-mid: #3f8db5;
  }
  * { box-sizing: border-box; margin: 0; padding: 0; }
  html, body {
    width: 1200px; height: 900px; overflow: hidden;
    background: var(--page-bg);
    font-family: "Open Sans", Arial, sans-serif;
    color: var(--ink);
  }
  .canvas { position: relative; width: 1200px; height: 900px; }
  .card {
    position: absolute; left: 250px;
    width: 700px; height: 400px;
    background: var(--card-bg);
    border-radius: 26px;
    overflow: hidden;
    box-shadow: 0 6px 18px rgba(0,0,0,0.12);
  }
  .card--front { top: 33px; }
  .card--back { top: 467px; }

  .brand { display: flex; align-items: center; gap: 14px; }
  .brand__mark {
    width: 52px; height: 52px; border-radius: 50%;
    background: var(--brand-mid); flex: none;
  }
  .brand__name {
    font-weight: 700; font-size: 19px; line-height: 1.15;
    color: var(--ink); text-transform: uppercase; letter-spacing: 0.5px;
    white-space: nowrap;
  }

  .card--front .brand {
    position: absolute; left: 0; right: 0; top: 150px;
    justify-content: center;
  }
  .slogan {
    position: absolute; left: 0; right: 0; top: 238px;
    text-align: center; font-weight: 400; font-size: 17px;
    letter-spacing: 1px; color: var(--ink-soft);
  }

  .card--back .brand { position: absolute; left: 36px; top: 180px; }
  .person { position: absolute; left: 310px; top: 74px; }
  .person__name {
    font-weight: 700; font-size: 30px; letter-spacing: 0.5px; line-height: 1.1;
  }
  .person__role {
    font-weight: 400; font-size: 15px; color: var(--brand-deep);
    letter-spacing: 0.5px; margin-top: 2px;
  }
  .contact {
    position: absolute; left: 310px; top: 170px;
    list-style: none; font-size: 13px; color: var(--ink-soft);
  }
  .contact__item {
    display: flex; align-items: center; gap: 8px; margin-bottom: 6px;
    white-space: nowrap;
  }
  .contact__icon { width: 14px; height: 14px; flex: none; }

  .band { position: absolute; left: 0; bottom: 0; width: 700px; height: 80px; }
</style>
</head>
<body>
<main class="canvas">

  <section class="card card--front" aria-label="Business card front">
    <div class="brand">
      <span class="brand__mark"></span>
      <span class="brand__name">Ridge 4 Ridge<br>Turbine Rentals</span>
    </div>
    <p class="slogan">CURRENT WHEREVER NEEDED</p>
  </section>

  <section class="card card--back" aria-label="Business card back">
    <div class="brand">
      <span class="brand__mark"></span>
      <span class="brand__name">Ridge 4 Ridge<br>Turbine Rentals</span>
    </div>

    <div class="person">
      <h1 class="person__name">MARK ELLISON</h1>
      <p class="person__role">DIRECTOR</p>
    </div>

    <ul class="contact">
      <li class="contact__item">
        <svg class="contact__icon" viewBox="0 0 14 14" aria-hidden="true">
          <rect x="3.5" y="1" width="7" height="12" rx="1.5" fill="none" stroke="#1f6a96" stroke-width="1.4"/>
          <line x1="6" y1="11" x2="8" y2="11" stroke="#1f6a96" stroke-width="1.2"/>
        </svg>
        <span>0481265390</span>
      </li>
      <li class="contact__item">
        <svg class="contact__icon" viewBox="0 0 14 14" aria-hidden="true">
          <rect x="1" y="3" width="12" height="8.5" rx="1" fill="none" stroke="#1f6a96" stroke-width="1.4"/>
          <polyline points="1.5,3.5 7,8 12.5,3.5" fill="none" stroke="#1f6a96" stroke-width="1.3"/>
        </svg>
        <span>bookings@ridge4ridgeturbinerentals-example.com.au</span>
      </li>
    </ul>

    <svg class="band" viewBox="0 0 700 80" aria-hidden="true">
      <rect x="0" y="64" width="700" height="16" fill="var(--brand-deep)"/>
      <rect x="330" y="28" width="80" height="36" fill="var(--brand-deep)"/>
      <rect x="410" y="28" width="240" height="36" fill="var(--brand-light)"/>
      <rect x="650" y="28" width="50" height="36" fill="var(--brand-deep)"/>
    </svg>
  </section>

</main>
</body>
</html>
```